Poster for a boatshow for Nautical enthusiasts, masculine and high incoming :-)

We need a poster for a boat show. Motorboats and Sailboats is presented in this Boat show (and other nautical topics like diving, wakeboard, kite, surf, fishing, ...)
This boat show is annual and the Poster is for the 2015 edition.

Your concept must be compatible in a landscape format. (We will ourselves adaptations of different formats.)
Width: 210 mm
Height: 297 mm
It's necessary for us to have the source file (vector) for make, later, the different format (flyers, website, ...)

Content of the Poster:
- 1 big picture (from a cheap stock, like Pixaloom.com) (NO CLIP ART) on full page or half page. Clip art must be a small detail added on the poster.
- Big title: « Foire fluviale des Ormeaux » (« du Léman » must be smaller of « Foire fluviale ».)
- Date: « 13, 14 et 15 novembre 2015 »
- Place: « Varimont - Genève »
- website: « www.foire-riveraine.ch » or « foire-riveraine.ch »
- Please, leave a zone in the poster for sponsors logos
- The « Jet d’eau de Genève » (http://en.wikifolio-example.org/wiki/Gerbe_Castelbrune) MUST be visible on the poster (in the picture, added like a clip art, or other graphic idea…)

Target Market(s)

Nautical enthusiasts, more masculine, high income.

Industry/Entity Type

Landscape

Font styles to use
Sans Serif

Colors
33a6d7
0892cd
ffffff

Requirements
Must have
• - The style must be modern, dynamic, bright colors, sober-minded.
• - "Jet d’eau de Genève" must be on the poster.
Should not have
• Clipart, cheap designs...
• Design with sea reference (sand, very big boats, ...). The market of the boatshow is around a lake (no sand, no boat more big of 15 meters).

```html
<!DOCTYPE html>
<html lang="fr">
<head>
<meta charset="utf-8">
<title>Foire fluviale des Ormeaux 2015</title>
<link rel="stylesheet" href="https://fonts.googleapis.com/css2?family=Montserrat:wght@400;600;700;800&display=swap">
<style>
  :root {
    --blue-panel: #0892cd;
    --blue-light: #33a6d7;
    --white: #ffffff;
    --sky: #d6e9f5;
    --water-deep: #0a5a98;
  }
  html, body {
    margin: 0;
    padding: 0;
    overflow: hidden;
    background: var(--white);
  }
  .poster {
    position: relative;
    width: 849px;
    height: 1200px;
    overflow: hidden;
    background: var(--blue-panel);
    font-family: "Montserrat", sans-serif;
    color: var(--white);
  }
  .hero-photo {
    position: absolute;
    left: 0;
    top: 0;
    width: 297px;
    height: 1200px;
    background: linear-gradient(180deg, var(--sky) 0%, #b5d6ec 30%, var(--blue-light) 55%, #1478b8 75%, var(--water-deep) 100%);
  }
  .venue {
    position: absolute;
    left: 334px;
    top: 30px;
    line-height: 1;
  }
  .venue-name {
    display: block;
    font-weight: 700;
    font-size: 30px;
    letter-spacing: 0.5px;
  }
  .venue-city {
    display: block;
    margin-top: 6px;
    font-weight: 400;
    font-size: 21px;
  }
  .title {
    position: absolute;
    left: 0;
    top: 0;
    width: 849px;
    height: 1200px;
  }
  .title text {
    font-family: "Montserrat", sans-serif;
    font-weight: 800;
    fill: var(--white);
  }
  .dates {
    position: absolute;
    left: 537px;
    top: 668px;
    font-weight: 700;
    line-height: 1;
  }
  .dates-day {
    display: block;
    font-size: 64px;
    line-height: 60px;
    letter-spacing: -1px;
  }
  .dates-month {
    display: block;
    margin-top: 14px;
    font-size: 29px;
  }
  .dates-year {
    display: block;
    margin-top: 6px;
    font-size: 27px;
    font-weight: 600;
  }
  .subtitle {
    position: absolute;
    left: 334px;
    top: 962px;
    font-weight: 700;
    font-size: 28px;
    letter-spacing: 0.5px;
  }
  .website {
    position: absolute;
    left: 345px;
    top: 1138px;
    font-weight: 600;
    font-size: 16px;
  }
</style>
</head>
<body>
  <main class="poster">
    <div class="hero-photo" role="img" aria-label="Voilier blanc naviguant au près sur un lac bleu sous un ciel clair"></div>

    <header class="venue">
      <span class="venue-name">VARIMONT</span>
      <span class="venue-city">Genève</span>
    </header>

    <svg class="title" viewBox="0 0 849 1200" aria-label="Foire fluviale">
      <text transform="translate(418 934) rotate(-90)" font-size="128" textLength="230" lengthAdjust="spacingAndGlyphs">FOIRE</text>
      <text transform="translate(524 742) rotate(-90)" font-size="128" textLength="567" lengthAdjust="spacingAndGlyphs">FLUVIALE</text>
    </svg>

    <div class="dates">
      <span class="dates-day">13</span>
      <span class="dates-day">14</span>
      <span class="dates-day">15</span>
      <span class="dates-month">NOVEMBRE</span>
      <span class="dates-year">// 2015</span>
    </div>

    <p class="subtitle" style="margin:0">DES ORMEAUX</p>

    <p class="website" style="margin:0">www.foire-riveraine.ch</p>
  </main>
</body>
</html>
```